Brightwell Amusements Investor Brochure

Start Up Company Brightwell Amusements requires 4 page A4 size brochure outlining and detailing new product. Draft layout attached. Information and points of difference included. Company logo and graphics attached. Final design should sell to investors.

```html
<!DOCTYPE html>
<html lang="en">
<head>
<meta charset="utf-8">
<title>Brightwell Amusements – Hospitals</title>
<link rel="stylesheet" href="https://fonts.googleapis.com/css2?family=Open+Sans:wght@400;600;700&display=swap">
<style>
  :root {
    --paper: #ffffff;
    --ink: #1a1a1a;
    --curve: #a6a6a6;
    --cell-blue: #5d8fd3;
    --cell-grey: #9d9d9d;
    --label-grey: #a4a4a4;
    --label-light: #cfcfcf;
    --frame: #333333;
    --band: #8c8c8c;
    --icon-blue: #5d8fd3;
    --photo-sky: #c9c4bc;
    --photo-building: #8a8e94;
  }
  * { margin: 0; padding: 0; box-sizing: border-box; }
  html, body { width: 849px; height: 1200px; overflow: hidden; background: var(--paper); }
  body { font-family: "Open Sans", sans-serif; color: var(--ink); }
  .page { position: relative; width: 849px; height: 1200px; overflow: hidden; }

  .guide-curves { position: absolute; left: 0; top: 0; width: 849px; height: 1200px; }

  .hero-photo {
    position: absolute; left: 135px; top: 88px; width: 640px; height: 240px;
    background: linear-gradient(180deg, var(--photo-sky) 0%, #b7b4ae 40%, var(--photo-building) 75%, #5a5d63 100%);
    box-shadow: 6px 8px 10px rgba(0,0,0,0.45);
  }

  .table-caption { position: absolute; left: 148px; top: 397px; font-size: 13px; }

  .stats-frame {
    position: absolute; left: 148px; top: 424px; width: 628px; height: 315px;
    border: 2px solid var(--frame); border-radius: 8px; background: var(--paper);
    box-shadow: 4px 6px 10px rgba(0,0,0,0.35);
  }
  .stats-grid {
    position: absolute; left: 7px; top: 16px;
    display: grid;
    grid-template-columns: 197px 38px 41px 46px 42px 42px 41px 41px 43px 42px;
    column-gap: 4px; row-gap: 3.6px;
    grid-auto-rows: 22px;
    font-size: 14.5px; color: #fff;
  }
  .stats-grid > span { display: flex; align-items: center; justify-content: center; }
  .stats-grid .label { justify-content: flex-start; padding-left: 3px; background: var(--label-grey); white-space: nowrap; }
  .stats-grid .label.section { font-style: italic; background: var(--label-light); color: #222; }
  .stats-grid .label.head { background: var(--label-light); }
  .stats-grid .label.total { background: var(--label-light); color: #111; font-weight: 700; }
  .stats-grid .b { background: var(--cell-blue); }
  .stats-grid .g { background: var(--cell-grey); }
  .stats-grid .bold { font-weight: 700; }

  .feature { position: absolute; display: flex; align-items: center; font-size: 29px; }
  .feature .marker { width: 31px; height: 31px; margin-right: 17px; flex: none; }
  .feature-1 { left: 157px; top: 818px; }
  .feature-2 { left: 180px; top: 899px; }
  .feature-3 { left: 203px; top: 981px; }

  .closing-band { position: absolute; left: 0; top: 1073px; width: 849px; height: 81px; }
  .closing-band p {
    position: absolute; inset: 0; display: flex; align-items: center; justify-content: center;
    color: #fff; font-size: 52px; padding-bottom: 4px;
  }
</style>
</head>
<body>
<div class="page">
  <svg class="guide-curves" viewBox="0 0 849 1200" aria-hidden="true">
    <g fill="none" stroke="var(--curve)" stroke-width="2">
      <path d="M188 0 C 30 300, 20 720, 160 835"/>
      <path d="M202 0 C 50 360, 50 800, 183 916"/>
      <path d="M218 0 C 75 420, 70 900, 206 998"/>
    </g>
  </svg>

  <div class="hero-photo" role="img" aria-label="Photograph of a modern hospital building with a car park entrance under a cloudy sky"></div>

  <p class="table-caption">Public and Private Hospitals, States and Territories, 2012-13</p>

  <div class="stats-frame">
    <div class="stats-grid">
      <span class="label head"></span><span class="b">NSW</span><span class="g">Vic</span><span class="b">Qld</span><span class="g">WA</span><span class="b">SA</span><span class="g">Tas</span><span class="b">ACT</span><span class="g">NT</span><span class="b">Total</span>
      <span class="label section">Public hospitals</span><span class="b"></span><span class="g"></span><span class="b"></span><span class="g"></span><span class="b"></span><span class="g"></span><span class="b"></span><span class="g"></span><span class="b"></span>
      <span class="label">Public acute hospitals</span><span class="b">218</span><span class="g">149</span><span class="b">166</span><span class="g">88</span><span class="b">78</span><span class="g">22</span><span class="b">3</span><span class="g">5</span><span class="b">729</span>
      <span class="label">Public psychiatric hospitals</span><span class="b">7</span><span class="g">1</span><span class="b">4</span><span class="g">2</span><span class="b">2</span><span class="g">1</span><span class="b">. .</span><span class="g">. .</span><span class="b">17</span>
      <span class="label">Total public hospitals</span><span class="b">225</span><span class="g">150</span><span class="b">170</span><span class="g">90</span><span class="b">80</span><span class="g">23</span><span class="b">3</span><span class="g">5</span><span class="b">746</span>
      <span class="label section">Private hospitals</span><span class="b"></span><span class="g"></span><span class="b"></span><span class="g"></span><span class="b"></span><span class="g"></span><span class="b"></span><span class="g"></span><span class="b"></span>
      <span class="label">Private free-standing day</span><span class="b">96</span><span class="g">85</span><span class="b">52</span><span class="g">35</span><span class="b">26</span><span class="g">0</span><span class="b">0</span><span class="g">0</span><span class="b">311</span>
      <span class="label">Other private hospitals</span><span class="b">89</span><span class="g">79</span><span class="b">53</span><span class="g">22</span><span class="b">28</span><span class="g">0</span><span class="b">0</span><span class="g">0</span><span class="b">281</span>
      <span class="label">Total private hospitals</span><span class="b">185</span><span class="g">164</span><span class="b">105</span><span class="g">57</span><span class="b">54</span><span class="g">0</span><span class="b">0</span><span class="g">0</span><span class="b">592</span>
      <span class="label"></span><span class="b"></span><span class="g"></span><span class="b"></span><span class="g"></span><span class="b"></span><span class="g"></span><span class="b"></span><span class="g"></span><span class="b"></span>
      <span class="label total">All hospitals</span><span class="b bold">410</span><span class="g bold">314</span><span class="b bold">275</span><span class="g bold">147</span><span class="b bold">134</span><span class="g bold">0</span><span class="b bold">0</span><span class="g bold">0</span><span class="b bold">1,338</span>
    </div>
  </div>

  <div class="feature feature-1">
    <svg class="marker" viewBox="0 0 31 31" aria-hidden="true"><rect x="1.5" y="1.5" width="28" height="28" rx="3" fill="var(--icon-blue)" stroke="#2c3e5c" stroke-width="2"/><path d="M11 8 L23 15.5 L11 23 Z" fill="#fff"/></svg>
    <span>Movies for hospitals</span>
  </div>
  <div class="feature feature-2">
    <svg class="marker" viewBox="0 0 31 31" aria-hidden="true"><rect x="1.5" y="1.5" width="28" height="28" rx="3" fill="var(--icon-blue)" stroke="#2c3e5c" stroke-width="2"/><path d="M11 8 L23 15.5 L11 23 Z" fill="#fff"/></svg>
    <span>Download movies in under 3 minutes</span>
  </div>
  <div class="feature feature-3">
    <svg class="marker" viewBox="0 0 31 31" aria-hidden="true"><rect x="1.5" y="1.5" width="28" height="28" rx="3" fill="var(--icon-blue)" stroke="#2c3e5c" stroke-width="2"/><path d="M11 8 L23 15.5 L11 23 Z" fill="#fff"/></svg>
    <span>No Internet connection required</span>
  </div>

  <div class="closing-band">
    <svg viewBox="0 0 849 81" width="849" height="81" aria-hidden="true"><polygon points="78,0 776,0 849,81 0,81" fill="var(--band)"/></svg>
    <p>...and hospitals</p>
  </div>
</div>
</body>
</html>
```